Drywall plastering business card design

Attached is my new logo and a picture of my current business card. I would like my new logo incorporated in to the business card and also my website which is:
www.ridgecrestwallfinishers.co.nz
Industry/Entity Type
Business
Contact Information for Business Card
I would like a picture of my van and my new logo on my new business card. See attached files for pictures of my old business card, van picture and logo.
Colors
0555a3
ffffff
Requirements
Must have
- New logo, Van, contact info

```html
<!DOCTYPE html>
<html lang="en">
<head>
<meta charset="utf-8">
<title>Ridgecrest Wall Finishers – Business Card</title>
<link href="https://fonts.googleapis.com/css2?family=Arimo:ital,wght@0,400;0,700;1,700&display=swap" rel="stylesheet">
<style>
  :root {
    --brand-blue: #0555a3;
    --icon-blue: #1a7fd0;
    --ink: #3a3a3a;
    --ink-soft: #555555;
    --silver-dark: #d9d9d9;
    --silver-light: #ffffff;
    --white: #ffffff;
    --page: #ffffff;
  }
  html, body {
    margin: 0;
    padding: 0;
    width: 1200px;
    height: 812px;
    overflow: hidden;
    background: var(--page);
    font-family: "Arimo", Arial, sans-serif;
  }
  .card {
    position: absolute;
    left: 96px;
    top: 126px;
    width: 982px;
    height: 572px;
    overflow: hidden;
    background: linear-gradient(100deg, var(--silver-dark) 0%, #ececec 45%, var(--silver-light) 75%);
    box-shadow: 0 6px 18px rgba(0,0,0,0.28);
  }
  .card__band {
    position: absolute;
    left: 0;
    top: 0;
    width: 982px;
    height: 572px;
  }
  .person {
    position: absolute;
    left: 81px;
    top: 80px;
  }
  .person__name {
    margin: 0;
    font-size: 36px;
    font-weight: 700;
    color: var(--ink);
    line-height: 1;
  }
  .person__role {
    margin: 14px 0 0;
    font-size: 27px;
    color: var(--ink-soft);
    line-height: 1;
  }
  .contact {
    position: absolute;
    left: 81px;
    top: 208px;
    margin: 0;
    padding: 0;
    list-style: none;
  }
  .contact__item {
    display: flex;
    align-items: center;
    height: 54px;
    font-size: 30px;
    color: var(--ink);
  }
  .contact__item--phone { font-size: 32px; }
  .contact__icon {
    width: 30px;
    height: 30px;
    margin-right: 10px;
    flex: none;
  }
  .brand {
    position: absolute;
    left: 600px;
    top: 120px;
    width: 340px;
    display: flex;
    align-items: center;
    gap: 16px;
  }
  .brand__mark {
    width: 26px;
    height: 26px;
    background: var(--brand-blue);
    flex: none;
  }
  .brand__name {
    margin: 0;
    font-size: 40px;
    font-weight: 700;
    line-height: 1.05;
    color: var(--brand-blue);
  }
  .tagline {
    position: absolute;
    left: 0;
    width: 982px;
    top: 458px;
    margin: 0;
    text-align: center;
    font-size: 35px;
    font-weight: 700;
    font-style: italic;
    color: var(--white);
  }
</style>
</head>
<body>
  <div class="card">
    <svg class="card__band" viewBox="0 0 982 572" aria-hidden="true">
      <defs>
        <linearGradient id="silverSweep" x1="0" y1="0" x2="1" y2="0">
          <stop offset="0" stop-color="#9a9a9a"/>
          <stop offset="0.5" stop-color="#d4d4d4"/>
          <stop offset="1" stop-color="#8e8e8e"/>
        </linearGradient>
      </defs>
      <path d="M0 424 Q491 382 982 404 L982 572 L0 572 Z" fill="url(#silverSweep)"/>
      <path d="M0 438 Q491 398 982 420 L982 572 L0 572 Z" fill="var(--brand-blue)"/>
    </svg>

    <div class="person">
      <p class="person__name">Daniel Harper</p>
      <p class="person__role">Proprietor</p>
    </div>

    <ul class="contact">
      <li class="contact__item contact__item--phone">
        <svg class="contact__icon" viewBox="0 0 24 24" aria-hidden="true">
          <path d="M6.6 3.5 9 6.4c.4.5.3 1.1-.1 1.5L7.6 9.1c1 2.5 3 4.6 5.4 5.6l1.2-1.3c.4-.4 1-.5 1.5-.1l2.9 2.3c.5.4.5 1.1.1 1.6l-1.6 1.9c-.5.6-1.3.8-2 .6C9.7 18 5.9 14.2 4.2 8.8c-.2-.7 0-1.5.6-2l1.8-1.5c-.1-.6 0-.1 0-1.8z" fill="var(--icon-blue)"/>
        </svg>
        027 555 01 42
      </li>
      <li class="contact__item">
        <svg class="contact__icon" viewBox="0 0 24 24" aria-hidden="true">
          <rect x="3" y="6" width="18" height="12" rx="1" fill="none" stroke="var(--icon-blue)" stroke-width="2"/>
          <path d="M3.5 7 12 13l8.5-6" fill="none" stroke="var(--icon-blue)" stroke-width="2"/>
        </svg>
        ridgecrestwallfinishers@gmail.com
      </li>
      <li class="contact__item">
        <svg class="contact__icon" viewBox="0 0 24 24" aria-hidden="true">
          <circle cx="12" cy="12" r="8.5" fill="none" stroke="var(--icon-blue)" stroke-width="1.8"/>
          <ellipse cx="12" cy="12" rx="3.8" ry="8.5" fill="none" stroke="var(--icon-blue)" stroke-width="1.5"/>
          <path d="M3.5 12h17M5 7.5h14M5 16.5h14" stroke="var(--icon-blue)" stroke-width="1.5"/>
        </svg>
        www.ridgecrestwallfinishers.co.nz
      </li>
    </ul>

    <div class="brand">
      <span class="brand__mark" aria-hidden="true"></span>
      <p class="brand__name">Ridgecrest<br>Wall Finishers</p>
    </div>

    <p class="tagline">Large jobs or small - Always quality assured</p>
  </div>
</body>
</html>
```